CD Cover -Vekko - Copperwing (ft. Tiri Jal)

We need a CD Cover immediately. We are dissatisfied with our past and wish that someone can help us.

Teamed's "Copperwing" as single units as you can see, this template I sent to where you see the text that will be with.

We hope that you can help us with this promptly. We are looking for someone who is creative and can do anything on their own.

Industry/Entity Type

Music Download

Font styles to use
Decorative

Requirements
Must have
• Änvänd er kreativitet och gör det ni tror hade passat?
Nice to have
• Copperwing Cartoon jus
• 1400x1400
Should not have
• Copperwing

```html
<!DOCTYPE html>
<html lang="en">
<head>
<meta charset="utf-8">
<title>Copperwing – Single Cover</title>
<link href="https://fonts.googleapis.com/css2?family=Cinzel:wght@900&display=swap" rel="stylesheet">
<style>
  :root {
    --stage-grey: #808080;
    --deep-black: #0b0500;
    --burnt-amber: #6a3304;
    --rich-gold: #d99a12;
    --bright-gold: #ffd54a;
    --hot-white: #fff6d8;
    --title-edge: #2a1a00;
  }
  html, body {
    margin: 0;
    padding: 0;
    width: 1200px;
    height: 1000px;
    overflow: hidden;
    background: var(--stage-grey);
  }
  .canvas {
    position: relative;
    width: 1200px;
    height: 1000px;
    background: var(--stage-grey);
  }
  .cover {
    position: absolute;
    left: 367px;
    top: 267px;
    width: 467px;
    height: 467px;
    overflow: hidden;
  }
  .cover-art {
    position: absolute;
    inset: 0;
    background:
      radial-gradient(ellipse 30% 22% at 50% 48%, var(--hot-white) 0%, rgba(255,230,140,0.6) 40%, rgba(255,200,60,0) 100%),
      radial-gradient(ellipse 22% 18% at 96% 30%, rgba(255,240,200,0.9) 0%, rgba(255,180,60,0) 100%),
      radial-gradient(ellipse 20% 18% at 4% 72%, rgba(255,240,200,0.85) 0%, rgba(255,180,60,0) 100%),
      radial-gradient(ellipse 70% 60% at 52% 55%, var(--bright-gold) 0%, var(--rich-gold) 35%, var(--burnt-amber) 70%, var(--deep-black) 100%);
  }
  .title-band {
    position: absolute;
    left: 0;
    top: 468px;
    width: 1200px;
  }
  .title-band-svg {
    position: absolute;
    left: 0;
    top: 0;
    width: 467px;
    height: 80px;
  }
  .title-text {
    font-family: 'Cinzel', serif;
    font-weight: 900;
    font-size: 44px;
  }
</style>
</head>
<body>
  <div class="canvas">
    <div class="cover">
      <div class="cover-art" role="img" aria-label="Abstract swirling golden light with glowing sparkles and bokeh on a dark background"></div>
      <svg class="title-band-svg" style="top:196px" viewBox="0 0 467 80" aria-hidden="false">
        <defs>
          <linearGradient id="band-shade" x1="0" x2="1" y1="0" y2="0">
            <stop offset="0" stop-color="#000" stop-opacity="0"/>
            <stop offset="0.12" stop-color="#1a0d00" stop-opacity="0.75"/>
            <stop offset="0.88" stop-color="#1a0d00" stop-opacity="0.75"/>
            <stop offset="1" stop-color="#000" stop-opacity="0"/>
          </linearGradient>
          <linearGradient id="gold-face" x1="0" x2="0" y1="0" y2="1">
            <stop offset="0" stop-color="#fff3a8"/>
            <stop offset="0.45" stop-color="#f2c81c"/>
            <stop offset="0.55" stop-color="#b98506"/>
            <stop offset="1" stop-color="#ffe066"/>
          </linearGradient>
          <linearGradient id="shine-line" x1="0" x2="1">
            <stop offset="0" stop-color="#fff" stop-opacity="0"/>
            <stop offset="0.5" stop-color="#fff" stop-opacity="0.9"/>
            <stop offset="1" stop-color="#fff" stop-opacity="0"/>
          </linearGradient>
        </defs>
        <rect class="band-shade" x="20" y="10" width="447" height="48" fill="url(#band-shade)"/>
        <rect class="band-line" x="30" y="8" width="430" height="2" fill="url(#shine-line)"/>
        <rect class="band-line" x="40" y="56" width="427" height="2" fill="url(#shine-line)"/>
        <text class="title-text" x="48" y="50" textLength="363" lengthAdjust="spacingAndGlyphs"
              fill="url(#gold-face)" stroke="var(--title-edge)" stroke-width="1.5" paint-order="stroke">COPPERWING</text>
      </svg>
    </div>
  </div>
</body>
</html>
```